Soap box for artisan soaps, eco-look, high design

We need a soap box for our lovely artisan soaps. The box size is: 9 cm height x 6,5 cm width x 2,8 cm depth. It would be nice when there is a small window in the box so you can see the soap.

See attachment for an example soap box (upside down). Please use the same elements such as texts and industrie logos. The idea is that we have a generic design that we can custom-made for different soaps. We have 15 different soaps in total at the moment.

Target Market(s)

Middle to high income

Font styles to use
Decorative
Script

Requirements
Must have
• Dutch text:
• Etherische oliën
• Handgemaakt
• Natuurlijke ingrediënten

```html
<!DOCTYPE html>
<html lang="nl">
<head>
<meta charset="utf-8">
<title>Velmora – Lemon and Poppy soap box</title>
<link rel="stylesheet" href="https://fonts.googleapis.com/css2?family=Dancing+Script:wght@600&family=Cormorant+SC:wght@500;700&family=Courier+Prime:wght@700&family=Open+Sans:wght@400;600&display=swap">
<style>
  :root {
    --backdrop: #e4e5e7;
    --kraft: #c9a77c;
    --kraft-light: #d4b68e;
    --kraft-dark: #b7946a;
    --sage: #a9b9a0;
    --brand-blue: #1d5b85;
    --ink: #3b3530;
    --white: #ffffff;
    --soap-light: #e8a83a;
    --soap-dark: #c27a1c;
  }
  * { box-sizing: border-box; margin: 0; padding: 0; }
  html, body { width: 1200px; height: 857px; overflow: hidden; }
  body { background: var(--backdrop); font-family: "Open Sans", sans-serif; }
  .canvas { position: relative; width: 1200px; height: 857px; }

  .box-top {
    position: absolute; left: 200px; top: 70px; width: 800px; height: 470px;
    background: var(--kraft); border-radius: 4px 4px 0 0; overflow: hidden;
  }
  .botanical-texture {
    position: absolute; inset: 0;
    background:
      radial-gradient(ellipse 45% 55% at 72% 40%, rgba(169,185,160,0.45), transparent 70%),
      radial-gradient(ellipse 35% 45% at 25% 75%, rgba(212,182,142,0.7), transparent 70%),
      radial-gradient(ellipse 30% 40% at 90% 85%, rgba(169,185,160,0.3), transparent 70%);
  }
  .soap-window { position: absolute; left: 40px; top: 36px; width: 170px; height: 128px; }

  .brand-name {
    position: absolute; left: 290px; top: 52px; width: 220px; text-align: center;
    font-family: "Cormorant SC", serif; font-weight: 700; font-size: 54px;
    color: var(--brand-blue); letter-spacing: 1px; line-height: 1;
  }
  .product-name {
    position: absolute; left: 0; right: 0; top: 180px; text-align: center;
    font-family: "Dancing Script", cursive; font-weight: 600; font-size: 84px;
    color: var(--white); line-height: 1;
  }
  .claim-oils {
    position: absolute; left: 0; right: 0; top: 290px; text-align: center;
    font-family: "Cormorant SC", serif; font-weight: 500; font-size: 32px;
    color: var(--ink); letter-spacing: 3px; line-height: 1.2;
  }
  .claim-handmade {
    position: absolute; left: 0; right: 0; top: 343px; text-align: center;
    font-family: "Courier Prime", monospace; font-weight: 700; font-size: 20px;
    color: var(--ink); line-height: 1.2;
  }
  .claim-natural {
    position: absolute; left: 0; right: 0; top: 392px; text-align: center;
    font-family: "Open Sans", sans-serif; font-weight: 600; font-size: 22px;
    color: var(--ink); letter-spacing: 1px; line-height: 1.2;
  }

  .box-side {
    position: absolute; left: 200px; top: 540px; width: 800px; height: 170px;
    background: var(--kraft-dark); border-top: 2px solid var(--kraft-light);
    padding: 26px 40px;
  }
  .ingredients {
    font-size: 16px; line-height: 1.45; color: var(--ink); text-align: justify;
  }
</style>
</head>
<body>
<main class="canvas">
  <section class="box-top">
    <div class="botanical-texture" role="img" aria-label="Faint botanical line pattern of leaves and flowers"></div>

    <svg class="soap-window" viewBox="0 0 200 150" role="img" aria-label="Window showing the lemon and poppy seed soap bar">
      <defs>
        <linearGradient id="soapTone" x1="0" y1="0" x2="1" y2="1">
          <stop offset="0" stop-color="#e8a83a"/>
          <stop offset="1" stop-color="#c27a1c"/>
        </linearGradient>
      </defs>
      <path d="M6 40 Q6 6 40 6 L120 6 Q194 30 194 144 L6 144 Z"
            fill="url(#soapTone)" stroke="#ffffff" stroke-width="5"/>
    </svg>

    <div class="brand-name">Velmora</div>
    <h1 class="product-name">Lemon and Poppy</h1>
    <p class="claim-oils">ETHERISCHE OLIËN</p>
    <p class="claim-handmade">Handgemaakt</p>
    <p class="claim-natural">Natuurlijke ingrediënten</p>
  </section>

  <section class="box-side">
    <p class="ingredients">Ingredients: Olijf olie pomace (Olea europaea), Kokosnoot olie (Cocos nucifera), Palm olie (Elaeis Guineensis Kernel Oil), Water (Aqua), Citroen Etherische Olie (Citrus limonum), maanzaad (Papaver somniferum), Ijzer oxide geel (Iron Oxide) Natuurlijke bestanddelen van Etherische Olie – Citral, Citronellol, Geraniol, Limonene, Linalool.</p>
  </section>
</main>
</body>
</html>
```